VEXO requires an exciting new business card

New business card required for VEXO. We are a new market research consultancy and want our brand to be approachable and be contemporary/modern, bold, uncomplicated/simple, and use friendly and easy to read fonts.

A draft website front page is attached to give you a feel (the pictures will be improved over the coming days).

The business card will be printed on 600gsm card, full colour both sides. The card is unique in that it allows one of four colours to be placed within the seam of the card (see http://uk.tarnix.com/products/halo/business-cards.html)

The logo has been designed in yellow on white, white on yellow, yellow on black and black on yellow - please select whichever you feel most appropriate from the attached document (please use the versions with the tagline). I think my preference is yellow on white for the front, and then yellow or black as the dominant colour on the back.

Telephone numbers will be given next week as they are now being finalised.

Thanks

Target Market(s)

Professionals in large corporates, such as Marketing Managers at Bravik, Fizzor Dune, Domacore etc.

Industry/Entity Type

Market Research

Requirements
Must have
• Greg Hallow QPMR
vexo
Level 4, 17 Ember St
Quindle Park
NSW 2087
Tel: 02 XXXX XXXX
Mob: XXXX XXXXXX
Email: greg@vexomr.com.au
Web: www.vexomr.com.au

```html
<!DOCTYPE html>
<html lang="en">
<head>
<meta charset="utf-8">
<title>VEXO business card</title>
<link rel="stylesheet" href="https://fonts.googleapis.com/css2?family=Jost:wght@400;500&display=swap">
<style>
  :root {
    --brand-yellow: #fcd116;
    --charcoal: #29363a;
    --paper: #ffffff;
    --canvas: #ffffff;
    --edge: #1f2a2d;
  }
  * { box-sizing: border-box; margin: 0; padding: 0; }
  html, body {
    width: 1200px;
    height: 1000px;
    overflow: hidden;
    background: var(--canvas);
    font-family: "Jost", sans-serif;
  }
  .canvas { position: relative; width: 1200px; height: 1000px; }

  .card {
    position: absolute;
    width: 717px;
    height: 483px;
    overflow: hidden;
  }

  /* Brand name */
  .brand {
    position: absolute;
    left: 0;
    width: 100%;
    display: flex;
    align-items: center;
    justify-content: center;
  }
  .brand-name {
    font-weight: 500;
    line-height: 1;
    letter-spacing: 0.02em;
  }

  /* Back card */
  .card-back {
    left: 450px;
    top: 482px;
    background: var(--brand-yellow);
    color: var(--charcoal);
  }
  .card-back .brand { top: 0; height: 100%; }
  .card-back .brand-name { font-size: 210px; }

  /* Front card */
  .card-front {
    left: 47px;
    top: 42px;
    background: var(--paper);
    color: var(--charcoal);
    border: 1px solid var(--edge);
    z-index: 1;
  }
  .card-front .brand { top: 40px; height: 190px; color: var(--brand-yellow); }
  .card-front .brand-name { font-size: 165px; }

  .contact-main {
    position: absolute;
    top: 250px;
    left: 0;
    width: 100%;
    text-align: center;
  }
  .person-name { font-size: 37px; font-weight: 400; line-height: 1.2; }
  .phone { font-size: 29px; font-weight: 400; line-height: 1.22; }

  .contact-band {
    position: absolute;
    left: 0; bottom: 0;
    width: 100%;
    height: 108px;
    background: var(--charcoal);
    color: var(--paper);
    padding: 16px 28px 0;
    font-size: 26px;
    line-height: 1.38;
  }
  .band-row { display: flex; justify-content: space-between; }
  .address { font-size: 28px; }
</style>
</head>
<body>
<main class="canvas">

  <section class="card card-back" aria-label="Card back">
    <div class="brand">
      <span class="brand-name">VEXO</span>
    </div>
  </section>

  <section class="card card-front" aria-label="Card front">
    <div class="brand">
      <span class="brand-name">VEXO</span>
    </div>

    <div class="contact-main">
      <p class="person-name">Greg Hallow, QPMR</p>
      <p class="phone">Tel: 02 4630 7152</p>
      <p class="phone">Mob: 7391 528604</p>
    </div>

    <div class="contact-band">
      <div class="band-row">
        <span class="email">greg@vexomr.com.au</span>
        <span class="website">www.vexomr.com.au</span>
      </div>
      <p class="address">Level 4, 17 Ember St, Quindle Park, NSW 2087</p>
    </div>
  </section>

</main>
</body>
</html>
```